Vemb - Website Design in WordPress (2 pages)

The goal of this design work is to create two highly focused, PPC- and SEO-aware landing pages that clearly explain the experience in familiar terms and drive app installs. The design must respect the existing visual identity and support future iteration of copy and content without requiring redesign.
Required Deliverables:
Fully working WordPress site containing:
Homepage template
Location landing page template
Mobile-first, responsive
CTA behaviour exactly as designed
Required
WordPress admin access
Full site export / backup
Homepage template
Mobile-first behaviour
CTA visible above the fold on mobile
Uses my:
Visual identity
Logo
Placeholder copy
I receive:
Admin access
Full site export / backup
Not acceptable
20+ plugins
Proprietary or abandoned builders
Hardcoded layouts that can’t be reused
Separate page designs per location
Elementor is preferred if:
One builder only
Clean structure
No custom lock-in widgets
Uploaded the mobile design for inspiration only
Coding
Coded - Design and coding required
Look and feel
Each slider illustrates characteristics of the customer's brand and the style your logo design should communicate.

```html
<!DOCTYPE html>
<html lang="en">
<head>
<meta charset="utf-8">
<title>Vemb – Discover Outdoor Experiences</title>
<link href="https://fonts.googleapis.com/css2?family=Fredoka:wght@400;500;600&family=Poppins:wght@400;500;600&display=swap" rel="stylesheet">
<style>
:root{
  --teal:#177c89;
  --teal-dark:#115a66;
  --teal-deep:#0e4a55;
  --teal-soft:#d9f3ef;
  --orange:#f2612c;
  --orange-soft:#fde9dd;
  --peach:#fdf3ea;
  --ink:#1f2a30;
  --muted:#4d5a60;
  --line:#e6ecee;
  --white:#fff;
}
*{box-sizing:border-box;margin:0;padding:0}
html,body{width:1200px;height:4307px;overflow:hidden}
body{position:relative;background:var(--white);font-family:"Poppins",sans-serif;color:var(--ink)}
.abs{position:absolute}
h1,h2,h3,.brand,.stat-num{font-family:"Fredoka",sans-serif}
.brand{color:var(--teal);font-weight:600;letter-spacing:-1px}
.btn-outline{position:absolute;border:1.5px solid var(--orange);color:var(--orange);border-radius:22px;font-size:12px;font-weight:600;display:flex;align-items:center;justify-content:center;letter-spacing:.3px}
.section-title{position:absolute;left:0;width:1200px;text-align:center;color:var(--teal-dark);font-weight:500;font-size:40px}
.section-title .ul{position:relative;display:inline-block}
.section-title .ul::after{content:"";position:absolute;left:10%;right:10%;bottom:-6px;height:3px;border-radius:3px;background:var(--orange);transform:rotate(-1deg)}
.section-sub{position:absolute;left:0;width:1200px;text-align:center;font-size:13px;color:var(--ink);line-height:24px}

/* header & hero */
.hero-bg{left:0;top:0;width:1200px;height:700px;background:linear-gradient(180deg,#fff 0%,#fff 60%,#f5fbfa 100%)}
.logo{left:140px;top:18px;font-size:60px;line-height:60px}
.nav-home{left:870px;top:26px;font-size:14px;font-weight:500}
.nav-loc{left:950px;top:15px;width:112px;height:42px;border-radius:21px;background:var(--orange);color:#fff;font-size:13px;font-weight:500;display:flex;align-items:center;justify-content:center}
.pill{left:142px;top:134px;height:36px;padding:0 20px;border-radius:18px;background:var(--orange-soft);color:var(--orange);font-size:12px;display:flex;align-items:center}
.hero-title{left:140px;top:186px;font-size:57px;line-height:59px;font-weight:400;color:var(--teal-dark)}
.hero-title .hl{color:var(--orange);font-weight:600}
.hero-text{left:142px;top:374px;width:440px;font-size:12px;line-height:24px}
.store{height:52px;border-radius:8px;background:#111}
.hero-meta{left:140px;top:548px;display:flex;gap:26px;font-size:11.5px;align-items:center}
.hero-meta span{display:flex;align-items:center;gap:8px}
.hero-visual{left:618px;top:84px;width:520px;height:520px;border-radius:50%;background:radial-gradient(circle at 40% 40%,#b78a55,#5b4330 60%,#2c2a26);overflow:hidden}
.phone{left:754px;top:128px;width:250px;height:505px;border-radius:38px;background:linear-gradient(180deg,#1d7f8c 0%,#1d7f8c 30%,#f4f6f7 30%,#f4f6f7 100%);border:8px solid #1a1a1a}

/* comparison */
.cmp-card{background:#fff;border:1px solid var(--line);border-radius:14px}
.cmp-hi{background:var(--teal);border-radius:14px;box-shadow:0 10px 30px rgba(17,90,102,.25)}
.col{position:absolute;top:970px;width:260px}
.col .icon{width:56px;height:56px;border-radius:50%;background:#5fc5c7;display:flex;align-items:center;justify-content:center;margin-bottom:18px}
.col h3{font-size:19px;font-weight:500;color:var(--teal-dark)}
.col .desc{font-size:11.5px;line-height:20px;margin-top:8px;color:var(--muted);height:50px}
.col ul{list-style:none}
.col li{height:42px;display:flex;align-items:center;gap:10px;font-size:12px;border-top:1px solid var(--line)}
.col li:first-child{border-top:none}
.col.light h3,.col.light .desc,.col.light li{color:#fff}
.col.light li{border-top-color:rgba(255,255,255,.25)}
.col.light .icon{background:#fff}

/* how */
.peach{left:0;top:1410px;width:1200px;height:660px}
.feat{position:absolute;width:414px;height:120px;background:#fff;border-radius:20px;box-shadow:0 6px 24px rgba(0,0,0,.06);padding:18px 20px 0 0}
.feat h3{font-size:19px;font-weight:500;color:var(--teal-dark)}
.feat p{font-size:11.5px;line-height:20px;margin-top:6px;color:var(--muted)}
.ficon{position:absolute;width:70px;height:70px;border-radius:50%;display:flex;align-items:center;justify-content:center}

/* steps */
.step{position:absolute;top:2246px;width:190px;text-align:center}
.step .badge-wrap{position:relative;width:104px;height:104px;margin:0 auto}
.step .sicon{width:104px;height:104px;border-radius:50%;background:#fff;box-shadow:0 8px 22px rgba(0,0,0,.08);display:flex;align-items:center;justify-content:center}
.step .num{position:absolute;right:-4px;top:-4px;width:30px;height:30px;border-radius:50%;background:var(--teal);color:#fff;font-size:12px;font-weight:600;display:flex;align-items:center;justify-content:center;border:3px solid #fff}
.step h3{margin-top:26px;font-size:20px;line-height:24px;font-weight:500;color:var(--teal)}
.step p{margin-top:10px;font-size:11px;line-height:17px;color:var(--muted)}

/* stats & reviews */
.stat{position:absolute;top:2874px;width:198px;height:98px;background:#fff;border-radius:10px;box-shadow:0 6px 22px rgba(0,0,0,.06);text-align:center;padding-top:18px}
.stat-num{font-size:28px;font-weight:600;color:#111}
.stat-lbl{font-size:13px;margin-top:2px}
.review{position:absolute;top:3008px;width:288px;height:280px;background:#fff;border-radius:14px;box-shadow:0 6px 24px rgba(0,0,0,.07);padding:20px}
.review .head{display:flex;align-items:center;gap:14px}
.avatar{width:56px;height:56px;border-radius:50%;background:linear-gradient(135deg,#e9c7a8,#8a6446)}
.review .name{font-family:"Fredoka",sans-serif;font-size:17px;font-weight:500}
.review .city{font-size:11.5px;color:var(--muted)}
.review .quote{position:absolute;right:22px;top:18px;font-family:"Fredoka",sans-serif;font-size:52px;line-height:52px;color:#5fc5c7;font-weight:600}
.stars{color:#f5a623;font-size:16px;letter-spacing:2px;margin:16px 0 6px}
.review p{font-size:11.5px;line-height:21px;color:var(--muted)}
.arrow{position:absolute;top:3129px;width:36px;height:36px;border-radius:50%;display:flex;align-items:center;justify-content:center}

/* cta */
.cta-card{left:142px;top:3430px;width:916px;height:405px;border-radius:28px;background:linear-gradient(100deg,#f58a5a 0%,#fbe0cb 38%,#fbf5ee 60%,#bff0e4 100%)}
.cta-photo{left:168px;top:3366px;width:400px;height:469px;border-radius:200px 200px 0 0;background:linear-gradient(180deg,#3a2418 0%,#b06a48 35%,#e6a9c0 65%,#d68aa6 100%)}
.cta-title{left:620px;top:3490px;font-size:50px;line-height:52px;font-weight:500;color:var(--teal-dark)}
.cta-text{left:622px;top:3624px;width:360px;font-size:12.5px;line-height:25px}

/* footer */
.footer{left:0;top:3880px;width:1200px;height:427px}
.fcontact{position:absolute;top:4110px;display:flex;align-items:center;gap:14px;color:#fff;font-size:12px;line-height:19px}
.fcontact .ic{width:42px;height:42px;border-radius:50%;background:#fff;display:flex;align-items:center;justify-content:center}
.flogo{left:500px;top:4098px;width:200px;text-align:center;font-size:78px;line-height:80px;color:#fff}
.fline{left:140px;top:4239px;width:920px;height:1px;background:rgba(255,255,255,.2)}
.copy{left:140px;top:4268px;font-size:11px;color:#fff}
.social{position:absolute;top:4264px;width:28px;height:28px;border-radius:50%;border:1.5px solid #fff}
</style>
</head>
<body>

<!-- Header & hero -->
<div class="abs hero-bg"></div>
<svg class="abs" style="left:0;top:540px" width="1200" height="170" viewBox="0 0 1200 170" aria-hidden="true">
  <defs><linearGradient id="heroWave" x1="0" x2="1"><stop offset="0" stop-color="#fff"/><stop offset=".45" stop-color="#c9f0e6"/><stop offset="1" stop-color="#e9f8f5"/></linearGradient></defs>
  <path d="M0 80 C200 150 400 170 620 120 C820 70 1000 30 1200 40 L1200 0 L0 0Z" fill="#fff"/>
  <path d="M0 80 C200 150 400 170 620 120 C820 70 1000 30 1200 40 L1200 170 L0 170Z" fill="url(#heroWave)" opacity=".7"/>
  <path d="M0 120 C300 170 700 170 1200 110 L1200 170 L0 170Z" fill="#fff"/>
</svg>

<div class="abs brand logo">Vemb</div>
<div class="abs nav-home">HOME</div>
<div class="abs nav-loc">LOCATIONS</div>

<div class="abs pill">Now Available in 12+ Cities</div>
<h1 class="abs hero-title">Discover Outdoor<br><span class="hl">Experiences</span><br>Near You</h1>
<svg class="abs" style="left:575px;top:182px" width="48" height="40" aria-hidden="true"><path d="M6 22 L10 4 M16 26 L30 10 M22 34 L42 24" stroke="#f2612c" stroke-width="2.5" stroke-linecap="round"/></svg>
<p class="abs hero-text">Download the VEMB app for outdoor group adventures. Walk between real locations, follow engaging stories, and play with friends - no host, no equipment, no fixed schedule.</p>
<div class="abs store" style="left:140px;top:465px;width:186px" role="img" aria-label="App store download badge"></div>
<div class="abs store" style="left:338px;top:465px;width:184px" role="img" aria-label="Play store download badge"></div>
<div class="abs hero-meta">
  <span><svg width="18" height="18" viewBox="0 0 24 24"><path d="M12 2l3 7 7 .6-5.4 4.7 1.7 7.2L12 17.8 5.7 21.5l1.7-7.2L2 9.6 9 9z" fill="#177c89"/></svg>4.9 Rating</span>
  <span><svg width="22" height="18" viewBox="0 0 26 20"><circle cx="9" cy="6" r="4" fill="#177c89"/><path d="M1 19c0-5 4-7 8-7s8 2 8 7z" fill="#177c89"/><circle cx="18" cy="5" r="3" fill="#177c89"/><path d="M18 10c4 0 7 2 7 7h-6" fill="#177c89"/></svg>1K+ Users</span>
  <span><svg width="18" height="18" viewBox="0 0 24 24" fill="none" stroke="#177c89" stroke-width="2.2" stroke-linecap="round"><path d="M12 3v12M7 10l5 5 5-5M4 20h16"/></svg>Free to Download</span>
</div>
<div class="abs hero-visual" role="img" aria-label="Vintage map with compass, photographed backdrop"></div>
<div class="abs phone" role="img" aria-label="App home screen showing player profile, announcement and featured nearby games"></div>

<!-- Comparison -->
<h2 class="section-title" style="top:775px"><span class="ul">Not Your Typical City Experience</span></h2>
<p class="section-sub" style="top:850px">VEMB combines the best elements of escape rooms, treasure hunts, and city<br>tours into one seamless outdoor adventure.</p>

<div class="abs cmp-card" style="left:157px;top:947px;width:884px;height:354px"></div>
<div class="abs cmp-hi" style="left:447px;top:926px;width:290px;height:398px"></div>

<div class="col" style="left:174px">
  <div class="icon"><svg width="28" height="28" viewBox="0 0 24 24" fill="none" stroke="#fff" stroke-width="2"><path d="M5 21V8a7 7 0 0114 0v13M9 21v-8h6v8"/></svg></div>
  <h3>Escape Rooms</h3>
  <p class="desc">Indoor puzzles in a confined space with time pressure and required bookings.</p>
  <ul>
    <li><svg width="16" height="16" viewBox="0 0 24 24"><path d="M4 12l5 5L20 6" stroke="#2a9d3c" stroke-width="3" fill="none"/></svg>Immersive puzzles</li>
    <li><svg width="14" height="14" viewBox="0 0 24 24"><path d="M5 5l14 14M19 5L5 19" stroke="#e23a2e" stroke-width="3.5"/></svg>Indoor only</li>
    <li><svg width="14" height="14" viewBox="0 0 24 24"><path d="M5 5l14 14M19 5L5 19" stroke="#e23a2e" stroke-width="3.5"/></svg>Fixed time slots</li>
    <li><svg width="14" height="14" viewBox="0 0 24 24"><path d="M5 5l14 14M19 5L5 19" stroke="#e23a2e" stroke-width="3.5"/></svg>Booking required</li>
  </ul>
</div>
<div class="col light" style="left:463px">
  <div class="icon"><svg width="26" height="26" viewBox="0 0 24 24" fill="none" stroke="#177c89" stroke-width="2.4"><circle cx="12" cy="12" r="8"/></svg></div>
  <h3>VEMB Experience</h3>
  <p class="desc">Outdoor adventures across real city streets with stories, puzzles, and flexibility.</p>
  <ul>
    <li><svg width="16" height="16" viewBox="0 0 24 24"><path d="M4 12l5 5L20 6" stroke="#fff" stroke-width="3" fill="none"/></svg>Immersive outdoor stories</li>
    <li><svg width="16" height="16" viewBox="0 0 24 24"><path d="M4 12l5 5L20 6" stroke="#fff" stroke-width="3" fill="none"/></svg>Real city exploration</li>
    <li><svg width="16" height="16" viewBox="0 0 24 24"><path d="M4 12l5 5L20 6" stroke="#fff" stroke-width="3" fill="none"/></svg>Play at your own pace</li>
    <li><svg width="16" height="16" viewBox="0 0 24 24"><path d="M4 12l5 5L20 6" stroke="#fff" stroke-width="3" fill="none"/></svg>No booking required</li>
  </ul>
</div>
<div class="col" style="left:766px">
  <div class="icon"><svg width="28" height="28" viewBox="0 0 24 24" fill="none" stroke="#fff" stroke-width="2"><rect x="4" y="4" width="10" height="12" rx="1"/><path d="M18 8v13M4 20h16"/></svg></div>
  <h3>City Tours</h3>
  <p class="desc">Indoor puzzles in a confined space with time pressure and required bookings.</p>
  <ul>
    <li><svg width="16" height="16" viewBox="0 0 24 24"><path d="M4 12l5 5L20 6" stroke="#2a9d3c" stroke-width="3" fill="none"/></svg>Visit landmarks</li>
    <li><svg width="14" height="14" viewBox="0 0 24 24"><path d="M5 5l14 14M19 5L5 19" stroke="#e23a2e" stroke-width="3.5"/></svg>Passive experience</li>
    <li><svg width="14" height="14" viewBox="0 0 24 24"><path d="M5 5l14 14M19 5L5 19" stroke="#e23a2e" stroke-width="3.5"/></svg>No game elements</li>
    <li><svg width="14" height="14" viewBox="0 0 24 24"><path d="M5 5l14 14M19 5L5 19" stroke="#e23a2e" stroke-width="3.5"/></svg>Fixed routes</li>
  </ul>
</div>
<div class="btn-outline" style="left:540px;top:1360px;width:120px;height:40px">APP INSTALL</div>

<!-- How you experience -->
<svg class="abs peach" viewBox="0 0 1200 660" preserveAspectRatio="none" aria-hidden="true">
  <defs><linearGradient id="peachG" x1="0" y1="0" x2="0" y2="1"><stop offset="0" stop-color="#fdf0e2"/><stop offset="1" stop-color="#fdf6ef"/></linearGradient></defs>
  <path d="M0 10 C220 40 300 120 560 100 C820 80 950 -10 1200 20 L1200 600 C900 660 600 560 300 610 C160 630 60 620 0 610Z" fill="url(#peachG)"/>
</svg>
<h2 class="section-title" style="top:1598px"><span class="ul">How You Experience VEMB</span></h2>
<p class="section-sub" style="top:1672px">A seamless outdoor game that transforms your city into an interactive adventure with friends.</p>

<div class="feat" style="left:162px;top:1726px;padding-left:68px">
  <h3>Local Experiences</h3>
  <p>Discover curated activities and hidden gems in your city that match your interests and preferences.</p>
</div>
<div class="feat" style="left:162px;top:1873px;padding-left:68px">
  <h3>Play with Friends Outdoors</h3>
  <p>Walk between real locations while following a story delivered through the app. Collaborate to solve puzzles and progress.</p>
</div>
<div class="feat" style="left:623px;top:1726px;padding-left:22px;padding-right:68px">
  <h3>Choose Your City Adventure</h3>
  <p>Select from available experiences in your city. Each offers a unique story, route, and set of challenges to solve.</p>
</div>
<div class="feat" style="left:623px;top:1873px;padding-left:22px;padding-right:68px">
  <h3>Complete at Your Own Pace</h3>
  <p>No fixed time slots or physical host required. Start, pause, and finish on your schedule. Typically 2-3 hours to complete.</p>
</div>
<div class="ficon" style="left:142px;top:1750px;background:#f6961e"><svg width="34" height="34" viewBox="0 0 24 24" fill="none" stroke="#fff" stroke-width="2"><path d="M12 21s-7-6-7-11a7 7 0 0114 0c0 5-7 11-7 11z"/><circle cx="12" cy="10" r="2.5"/></svg></div>
<div class="ficon" style="left:142px;top:1898px;background:#5fc5c7"><svg width="34" height="34" viewBox="0 0 24 24" fill="none" stroke="#fff" stroke-width="2"><circle cx="12" cy="12" r="8"/><circle cx="12" cy="12" r="3"/></svg></div>
<div class="ficon" style="left:988px;top:1750px;background:var(--teal)"><svg width="34" height="34" viewBox="0 0 24 24" fill="none" stroke="#fff" stroke-width="2"><path d="M3 6l6-2 6 2 6-2v14l-6 2-6-2-6 2z"/><path d="M9 4v14M15 6v14"/></svg></div>
<div class="ficon" style="left:988px;top:1898px;background:var(--orange)"><svg width="34" height="34" viewBox="0 0 24 24" fill="none" stroke="#fff" stroke-width="2"><circle cx="12" cy="12" r="8"/><path d="M12 7v5l3 2"/></svg></div>
<div class="abs" style="left:566px;top:1818px;width:72px;height:72px;border-radius:50%;background:var(--teal);border:5px solid #fff"></div>

<!-- Steps -->
<h2 class="section-title" style="top:2104px"><span class="ul">Simple 4-Step Experience</span></h2>
<p class="section-sub" style="top:2177px">From download to completion, the process is designed to be intuitive and engaging.</p>
<svg class="abs" style="left:270px;top:2270px" width="660" height="40" aria-hidden="true"><path d="M10 30 C60 0 110 0 150 20 M260 20 C310 40 350 40 400 14 M510 20 C560 0 600 0 640 18" stroke="#9aa7ab" stroke-width="1.4" stroke-dasharray="5 5" fill="none"/></svg>

<div class="step" style="left:126px">
  <div class="badge-wrap"><div class="sicon"><svg width="46" height="46" viewBox="0 0 24 24" fill="none" stroke-width="2"><rect x="8" y="9" width="9" height="13" rx="2" stroke="#177c89"/><path d="M6 2v7M3 6l3 3 3-3" stroke="#f2612c"/></svg></div><div class="num">01</div></div>
  <h3>Download &amp;<br>Open</h3>
  <p>Install The App And Open It To See Available Experiences In Your Area.</p>
</div>
<div class="step" style="left:378px">
  <div class="badge-wrap"><div class="sicon"><svg width="46" height="46" viewBox="0 0 24 24" fill="none" stroke-width="2"><path d="M3 6l6-2v14l-6 2z" stroke="#f2612c"/><path d="M9 4l6 2v14l-6-2M15 6l6-2v14l-6 2" stroke="#177c89"/></svg></div><div class="num">02</div></div>
  <h3>Choose<br>Experience</h3>
  <p>Pick A Story Adventure Based On Your Location, Group Size, And Interest.</p>
</div>
<div class="step" style="left:630px">
  <div class="badge-wrap"><div class="sicon"><svg width="46" height="46" viewBox="0 0 24 24"><rect x="3" y="8" width="9" height="9" fill="#177c89"/><rect x="12" y="4" width="9" height="9" fill="#f2612c"/><rect x="12" y="13" width="6" height="6" fill="#177c89"/></svg></div><div class="num">03</div></div>
  <h3>Navigate<br>&amp; Play</h3>
  <p>Follow The Map To Real Locations, Solve Puzzles, And Advance The Story.</p>
</div>
<div class="step" style="left:879px">
  <div class="badge-wrap"><div class="sicon"><svg width="46" height="46" viewBox="0 0 24 24" fill="none" stroke-width="2"><circle cx="12" cy="10" r="5" stroke="#177c89"/><path d="M4 20h16" stroke="#f2612c"/><path d="M10 10l2 2 3-4" stroke="#f2612c"/></svg></div><div class="num">04</div></div>
  <h3>Complete<br>&amp; Share</h3>
  <p>Finish The Adventure At Your Own Pace And Share Your Experience.</p>
</div>
<div class="btn-outline" style="left:540px;top:2520px;width:120px;height:40px">APP INSTALL</div>

<!-- Trusted -->
<svg class="abs" style="left:0;top:2560px" width="1200" height="180" viewBox="0 0 1200 180" preserveAspectRatio="none" aria-hidden="true">
  <path d="M0 20 C300 80 700 -20 1200 40 L1200 180 L0 180Z" fill="#fdf7f1"/>
</svg>
<div class="abs" style="left:0;top:2740px;width:1200px;height:700px;background:linear-gradient(180deg,#fdf7f1,#fff 30%)"></div>
<h2 class="section-title" style="top:2738px"><span class="ul">Trusted by Thousands</span></h2>
<p class="section-sub" style="top:2812px">Join a growing community of outdoor enthusiasts across the UK.</p>

<div class="stat" style="left:180px"><div class="stat-num">1K+</div><div class="stat-lbl">App Downloads</div></div>
<div class="stat" style="left:394px"><div class="stat-num">4.9</div><div class="stat-lbl">App Store Rating</div></div>
<div class="stat" style="left:608px"><div class="stat-num">2K+</div><div class="stat-lbl">Bookings Made</div></div>
<div class="stat" style="left:822px"><div class="stat-num">88%</div><div class="stat-lbl">Satisfaction Rate</div></div>

<div class="review" style="left:142px">
  <div class="head"><div class="avatar" role="img" aria-label="Portrait of reviewer"></div><div><div class="name">Daniel P.</div><div class="city">Bristol</div></div></div>
  <div class="quote">”</div>
  <div class="stars">★★★★★</div>
  <p>"Found Amazing Trail Walks I Never Knew Existed In My Own City. The Booking Process Was Seamless And The Community Aspect Makes It Even Better. "Found Amazing Trail Walks I Never Knew Existed In My Own City. The Booking Process Was Seamless."</p>
</div>
<div class="review" style="left:456px">
  <div class="head"><div class="avatar" role="img" aria-label="Portrait of reviewer"></div><div><div class="name">Priya L.</div><div class="city">Cardiff</div></div></div>
  <div class="quote">”</div>
  <div class="stars">★★★★★</div>
  <p>""Perfect For Weekend Adventures. I've Met Great People Through Group Activities And Discovered Parts Of The City I'd Never Explored Before." "Perfect For Weekend Adventures. I've Met Great People Through Group Activities And Discovered Parts."</p>
</div>
<div class="review" style="left:770px">
  <div class="head"><div class="avatar" role="img" aria-label="Portrait of reviewer"></div><div><div class="name">Owen H.</div><div class="city">Bath</div></div></div>
  <div class="quote">”</div>
  <div class="stars">★★★★★</div>
  <p>"Finally An App That Makes It Easy To Try New Outdoor Activities. The Kayaking Experience In Bath Was Brilliant – Booked In Seconds! Finally An App That Makes It Easy To Try New Outdoor Activities. The Kayaking Experience In Bath Was Brilliant – Booked In Seconds!."</p>
</div>
<div class="arrow" style="left:86px;background:var(--teal-deep)"><svg width="16" height="16" viewBox="0 0 24 24" fill="none" stroke="#fff" stroke-width="2.5"><path d="M19 12H5M11 6l-6 6 6 6"/></svg></div>
<div class="arrow" style="left:1077px;background:var(--orange)"><svg width="16" height="16" viewBox="0 0 24 24" fill="none" stroke="#fff" stroke-width="2.5"><path d="M5 12h14M13 6l6 6-6 6"/></svg></div>

<!-- CTA -->
<div class="abs cta-card"></div>
<div class="abs cta-photo" role="img" aria-label="Smiling woman with curly hair and glasses looking at her phone"></div>
<h2 class="abs cta-title">Start Your City<br>Adventure Today</h2>
<p class="abs cta-text">Download the app and discover interactive stories and challenges in your city. No signup, no booking, just download and play.</p>
<div class="btn-outline" style="left:620px;top:3724px;width:120px;height:40px">APP INSTALL</div>

<!-- Footer -->
<svg class="abs footer" viewBox="0 0 1200 427" preserveAspectRatio="none" aria-hidden="true">
  <path d="M0 30 C200 -10 350 0 600 60 C850 120 1000 80 1200 40 L1200 427 L0 427Z" fill="#0e4a55"/>
</svg>
<div class="fcontact" style="left:258px">
  <div class="ic"><svg width="20" height="20" viewBox="0 0 24 24" fill="#0e4a55"><path d="M6.6 10.8a15 15 0 006.6 6.6l2.2-2.2a1 1 0 011-.25 11.4 11.4 0 003.6.6 1 1 0 011 1V20a1 1 0 01-1 1A17 17 0 013 4a1 1 0 011-1h3.5a1 1 0 011 1 11.4 11.4 0 00.6 3.6 1 1 0 01-.25 1z"/></svg></div>
  <div><div>Call Us</div><div>+123 555 0142</div></div>
</div>
<div class="abs brand flogo">Vemb</div>
<div class="fcontact" style="left:790px">
  <div class="ic"><svg width="20" height="20" viewBox="0 0 24 24" fill="none" stroke="#0e4a55" stroke-width="2"><rect x="3" y="5" width="18" height="14" rx="2"/><path d="M3 7l9 6 9-6"/></svg></div>
  <div><div>Email</div><div>info@vemb.com</div></div>
</div>
<div class="abs fline"></div>
<div class="abs copy">© 2026 VEMB. All Rights Reserved. | Privacy Policy | Terms Of Service</div>
<div class="social" style="left:914px;background:#5fc5c7;border-color:#5fc5c7"></div>
<div class="social" style="left:952px"></div>
<div class="social" style="left:990px"></div>
<div class="social" style="left:1028px"></div>

</body>
</html>
```